Graphic Design Project - Coffee Label

I am a coffee roasting business and I need a professional label design for my bag of coffee. this needs to be in a format that we can change the "title" or "weight" of the product frequently ourselves. We do have photoshop, but cannot create the project, but can edit if need be to print. Our labels are 3"x8". we will want the colors to bleed to the end. The labels are white and glossy, but i want the design to give the illusion that the color of the label is not evident. I have a logo. I do not want the design to have a border. Since the label is only 3" wide and 8" tall the design needs to be creative to look good. although coffee colors are ok, I want a lot more color to not be boring. We could frequently change the label size and would need to adjust accordingly from the current design.
Updates

Reason: I just decided to remove my refundable contract into committed payment to a designer. I would like a few more days to broadcast that option.

Target Market(s)

30-50 year olds that have money and want to buy quality

Industry/Entity Type

Business

Requirements
Must have
• we currently are using label 3" wide and 8" tall. First and foremost I need to be able to edit the words on the label. I will need to change the net wt and the coffee blend names. I would like the ability to change the size if need be. the company name is
1. Heron Ridge Coffee
2. Artisan Coffee Roasting
3. Needs to be a large space for a particular coffee name i.e Rain, Fern and Ember Blend. Use this blend, but I need to be able to edit it for other blends.
4. Under the blend it should say Whole Bean. Also need to be able to edit.
5. At the bottom it should say Roasted in Millbrook, Oregon. www.heronridgecoffee.example
6. Below the coffee name there should be Net Weight ie 16 oz (this also needs to be editable for us)
Nice to have
• I have a logo, but it can be different. Labels are white, but I don't want borders, and would like the colors to bleed and not to appear to be a white label. the bags are light grey/silver metallic. Although many use a lot of "coffee" colors for design, I do not. I have pics of coffee beans; it doesn't have to be used. I don't want to be just a block of a pic of beans. Other pics of coffee related ideas is fine with me. I don't need the brand to dominate the label. Bolder colors. I have attached roasting pics. These do not have to be used, but can. If used please edit out the extraneous background.
Should not have
• Do not use borders. I want the colors to bleed to the end. I don't want the white label to show through as though I have a typed page of print. I don't want just coffee colors used. I don't want light colors. I don't want a "square" looking format wherein everything is just line by line. Asymmetrical is ok.

```html
<!DOCTYPE html>
<html lang="en">
<head>
<meta charset="utf-8">
<title>Heron Ridge Coffee – Bag Label</title>
<link rel="stylesheet" href="https://fonts.googleapis.com/css2?family=Dosis:wght@700;800&display=swap">
<style>
  :root {
    --backdrop: #d9dadb;
    --sky-top: #b8302a;
    --sky-bottom: #d8852a;
    --moon-top: #b31e24;
    --moon-bottom: #86141a;
    --name-orange: #e27429;
    --bean-light: #e2872a;
    --bean-dark: #a8281a;
    --base-red: #a61c22;
    --title-yellow: #f7e100;
    --text-white: #ffffff;
  }
  html, body {
    margin: 0;
    width: 1200px;
    height: 1000px;
    overflow: hidden;
    background: var(--backdrop);
  }
  .label {
    position: absolute;
    left: 445px;
    top: 37px;
    width: 347px;
    height: 925px;
    box-shadow: 0 4px 18px rgba(0,0,0,0.18);
  }
  .label svg { display: block; }
  .brand-title {
    font-family: "Dosis", sans-serif;
    font-weight: 700;
    fill: var(--title-yellow);
    text-anchor: middle;
    font-size: 112px;
  }
  .brand-name-small {
    font-family: "Dosis", sans-serif;
    font-weight: 700;
    fill: var(--name-orange);
    font-size: 26px;
    letter-spacing: 2px;
    text-anchor: middle;
  }
  .info {
    font-family: "Dosis", sans-serif;
    font-weight: 700;
    fill: var(--text-white);
    text-anchor: middle;
  }
  .tagline { font-size: 27px; }
  .blend-name { font-size: 33px; font-weight: 800; }
  .grind { font-size: 23px; }
  .net-weight { font-size: 20px; }
  .origin { font-size: 19px; }
</style>
</head>
<body>
  <div class="label">
    <svg width="347" height="925" viewBox="0 0 347 925" xmlns="http://www.w3.org/2000/svg">
      <defs>
        <linearGradient id="sky" x1="0" y1="0" x2="0" y2="1">
          <stop offset="0" stop-color="var(--sky-top)"/>
          <stop offset="1" stop-color="var(--sky-bottom)"/>
        </linearGradient>
        <linearGradient id="moon" x1="0" y1="0" x2="0" y2="1">
          <stop offset="0" stop-color="var(--moon-top)"/>
          <stop offset="1" stop-color="var(--moon-bottom)"/>
        </linearGradient>
        <linearGradient id="beans" x1="0" y1="0" x2="0" y2="1">
          <stop offset="0" stop-color="var(--bean-light)"/>
          <stop offset="0.5" stop-color="#c4481d"/>
          <stop offset="1" stop-color="var(--bean-dark)"/>
        </linearGradient>
        <clipPath id="label-edge"><rect width="347" height="925"/></clipPath>
      </defs>

      <g clip-path="url(#label-edge)">
        <rect class="sky-band" width="347" height="420" fill="url(#sky)"/>
        <rect class="bean-field" y="420" width="347" height="505" fill="url(#beans)" role="img" aria-label="Close-up photograph of roasted coffee beans in warm orange light"/>

        <text class="brand-name-small" x="173" y="112">HERON RIDGE</text>

        <circle class="moon" cx="173" cy="438" r="258" fill="url(#moon)"/>
        <ellipse class="base-arc" cx="173" cy="1090" rx="330" ry="275" fill="var(--base-red)"/>

        <text class="brand-title" x="173" y="330">HERON</text>
        <text class="brand-title" x="173" y="455">RIDGE</text>
        <text class="brand-title" x="173" y="580">COFFEE</text>

        <text class="info tagline" x="178" y="625" textLength="300" lengthAdjust="spacingAndGlyphs">Artisan Coffee Roasting</text>
        <text class="info blend-name" x="178" y="736" textLength="285" lengthAdjust="spacingAndGlyphs">Rain, Fern &amp; Ember</text>
        <text class="info blend-name" x="173" y="768">Blend.</text>
        <text class="info grind" x="173" y="801" textLength="142" lengthAdjust="spacingAndGlyphs">Whole Bean</text>
        <text class="info net-weight" x="173" y="859" textLength="159" lengthAdjust="spacingAndGlyphs">Net Weight 16 oz</text>
        <text class="info origin" x="174" y="895" textLength="262" lengthAdjust="spacingAndGlyphs">Roasted in Millbrook, Oregon.</text>
        <text class="info origin" x="171" y="914" textLength="268" lengthAdjust="spacingAndGlyphs">www.heronridgecoffee.example</text>
      </g>
    </svg>
  </div>
</body>
</html>
```